Fontenot Bayou Grillhouse (Owners Card)

Need a classy, but modern business card. I have included a promotional card for the steakhouse. I need one for myself (the owner) that is more professional.

Target Market(s)

General Public

Industry/Entity Type

Food service

Contact Information for Business Card

Name, business address, phone number, email, logo

Font styles to use
Serif
Sans Serif
Decorative
Script

Requirements
Must have
• My name (Darvel Pruitt), business address (327 Oakmere Street), phone number (510) 493-2615, email (Dpruittkr4@mailvane.example. On the back of the card: Psalms 27 1 The LORD is my light and my salvation— whom shall I fear? The LORD is the stronghold of my life— of whom shall I be afraid? 2 When the wicked advance against me to devour me, it is my enemies and my foes who will stumble and fall. 3 Though an army besiege me, my heart will not fear; though war break out against me, even then I will be confident.
Nice to have
• Something that’s bold, but modern and professional.

```html
<!DOCTYPE html>
<html lang="en">
<head>
<meta charset="utf-8">
<title>Fontenot Bayou Grillhouse – Owner Business Card</title>
<link href="https://fonts.googleapis.com/css2?family=Montserrat:wght@400;500;600;800&display=swap" rel="stylesheet">
<style>
  :root {
    --backdrop: #222222;
    --card: #101010;
    --shadow-art: #050505;
    --white: #ffffff;
    --green: #8dc63f;
    --gold: #d9a72a;
    --red: #ff2a14;
    --orange: #ff6a1a;
    --amber: #f7a81b;
  }
  * { margin: 0; padding: 0; box-sizing: border-box; }
  html, body {
    width: 1200px; height: 1200px; overflow: hidden;
    background: var(--backdrop);
    font-family: "Montserrat", Arial, sans-serif;
    color: var(--white);
  }
  .card {
    position: absolute; left: 156px; width: 840px; height: 480px;
    background: var(--card); overflow: hidden;
  }
  .card--front { top: 94px; }
  .card--back { top: 625px; }

  .decor-art {
    position: absolute;
    background: radial-gradient(ellipse at 50% 55%, var(--shadow-art) 0%, var(--shadow-art) 45%, rgba(5,5,5,0) 72%);
  }
  .card--front .decor-art { left: -40px; top: 0; width: 660px; height: 500px; }
  .card--back .decor-art { left: 490px; top: 60px; width: 420px; height: 440px; }

  .owner { position: absolute; left: 49px; top: 68px; }
  .owner__name {
    font-size: 29px; line-height: 32px; letter-spacing: 0.5px;
  }
  .owner__first {
    font-weight: 800;
    background: linear-gradient(90deg, var(--green), var(--gold) 50%, var(--red));
    -webkit-background-clip: text; background-clip: text; color: transparent;
  }
  .owner__last {
    font-weight: 400;
    background: linear-gradient(90deg, var(--red), var(--amber));
    -webkit-background-clip: text; background-clip: text; color: transparent;
  }
  .owner__email {
    margin-top: 10px; font-size: 14px; font-weight: 500; letter-spacing: 4.6px;
  }

  .brand {
    position: absolute; display: flex; flex-direction: column; align-items: center; gap: 10px;
    color: var(--orange); font-weight: 600; text-align: center;
  }
  .brand__dot { border-radius: 50%; background: var(--orange); }
  .card--front .brand { left: 583px; top: 38px; width: 222px; font-size: 19px; line-height: 24px; }
  .card--front .brand__dot { width: 58px; height: 58px; }
  .card--back .brand { left: 72px; top: 130px; width: 330px; font-size: 28px; line-height: 34px; }
  .card--back .brand__dot { width: 80px; height: 80px; }

  .contact { position: absolute; right: 30px; top: 355px; text-align: right; }
  .contact__row {
    display: flex; justify-content: flex-end; align-items: center; gap: 22px;
    height: 32px; font-size: 22px;
  }
  .contact__phone { font-weight: 800; }
  .contact__phone-end { color: var(--orange); }
  .contact__address { font-weight: 600; }
  .contact__icon { width: 20px; height: 20px; flex: none; }
  .accent-rule {
    position: absolute; left: 556px; top: 433px; width: 284px; height: 3px;
    background: linear-gradient(90deg, var(--amber), var(--red) 55%, var(--green));
  }

  .divider {
    position: absolute; left: 411px; top: 114px; width: 2px; height: 290px;
    background: linear-gradient(180deg, rgba(255,255,255,0), rgba(255,255,255,0.55) 50%, rgba(255,255,255,0));
  }
  .scripture { position: absolute; left: 451px; top: 124px; width: 330px; }
  .scripture__title {
    font-size: 18px; font-weight: 800; letter-spacing: 0.3px;
    background: linear-gradient(90deg, var(--green), var(--red) 50%, var(--amber));
    -webkit-background-clip: text; background-clip: text; color: transparent;
    display: inline-block;
  }
  .scripture__verses { list-style: none; margin-top: 26px; }
  .scripture__verse {
    position: relative; padding-left: 23px; margin-bottom: 29px;
    font-size: 10.6px; line-height: 12.6px; font-weight: 500; text-transform: uppercase;
  }
  .scripture__verse::before {
    content: ""; position: absolute; left: 0; top: 9px;
    width: 9px; height: 9px; border-radius: 50%; background: var(--white);
  }
</style>
</head>
<body>

<section class="card card--front">
  <div class="decor-art" role="img" aria-label="Large faint masquerade mask decoration"></div>

  <div class="owner">
    <h1 class="owner__name"><span class="owner__first">DARVEL</span> <span class="owner__last">PRUITT</span></h1>
    <p class="owner__email">DPRUITTKR4@MAILVANE.EXAMPLE</p>
  </div>

  <div class="brand">
    <span class="brand__dot"></span>
    <span class="brand__name">FONTENOT BAYOU GRILLHOUSE</span>
  </div>

  <div class="contact">
    <p class="contact__row">
      <span class="contact__phone">(510) 493-<span class="contact__phone-end">2615</span></span>
      <svg class="contact__icon" viewBox="0 0 24 24" aria-hidden="true"><path fill="#fff" d="M6.6 10.8a15.1 15.1 0 0 0 6.6 6.6l2.2-2.2a1 1 0 0 1 1-.25 11.4 11.4 0 0 0 3.6.57 1 1 0 0 1 1 1V20a1 1 0 0 1-1 1A17 17 0 0 1 3 4a1 1 0 0 1 1-1h3.5a1 1 0 0 1 1 1c0 1.25.2 2.45.57 3.57a1 1 0 0 1-.25 1z"/></svg>
    </p>
    <p class="contact__row">
      <span class="contact__address">327 OAKMERE STREET</span>
      <svg class="contact__icon" viewBox="0 0 24 24" aria-hidden="true"><path fill="none" stroke="#fff" stroke-width="2" d="M12 22s7-6.5 7-12a7 7 0 0 0-14 0c0 5.5 7 12 7 12z"/><path fill="#fff" d="M12 6.5l3.5 3v3.5h-7V9.5z"/></svg>
    </p>
  </div>
  <div class="accent-rule"></div>
</section>

<section class="card card--back">
  <div class="decor-art" role="img" aria-label="Faint masquerade mask decoration"></div>

  <div class="brand">
    <span class="brand__dot"></span>
    <span class="brand__name">FONTENOT BAYOU GRILLHOUSE</span>
  </div>

  <div class="divider"></div>

  <div class="scripture">
    <h2 class="scripture__title">PSALMS 27</h2>
    <ul class="scripture__verses">
      <li class="scripture__verse">The Lord is my light and my salvation— whom shall I fear? The Lord is the stronghold of my life— of whom shall I be afraid?</li>
      <li class="scripture__verse">When the wicked advance against me to devour me, it is my enemies and my foes who will stumble and fall.</li>
      <li class="scripture__verse">Though an army besiege me, my heart will not fear; though war break out against me, even then I will be confident.</li>
    </ul>
  </div>
</section>

</body>
</html>
```